Google slides for an upcoming presentation

I would like to recreate the jpeg to better match our company branding & color, as well as better resolution-- which is found in the PPTX. The slide should read....
"What are the biggest differences between Web 2.0 to Web 3.0"

Industry/Entity Type

Web3

Other font styles liked:
• Manrope

```html
<!DOCTYPE html>
<html lang="en">
<head>
<meta charset="utf-8">
<title>Web 2.0 to Web 3.0</title>
<link rel="stylesheet" href="https://fonts.googleapis.com/css2?family=Manrope:wght@500&family=Source+Sans+3:wght@400&display=swap">
<style>
  :root {
    --blue-deep: #0a1466;
    --blue-mid: #0530c8;
    --blue-glow: #2a6dff;
    --green: #3bdb62;
    --orange: #fa861c;
    --white: #ffffff;
  }
  html, body {
    margin: 0;
    padding: 0;
    width: 1200px;
    height: 675px;
    overflow: hidden;
  }
  .slide {
    position: relative;
    width: 1200px;
    height: 675px;
    overflow: hidden;
    background:
      radial-gradient(ellipse 60% 45% at 50% 0%, var(--blue-glow) 0%, var(--blue-mid) 45%, transparent 100%),
      linear-gradient(180deg, var(--blue-mid) 0%, #0420a0 45%, var(--blue-deep) 100%);
  }
  .wave-texture {
    position: absolute;
    left: 0;
    top: 130px;
    width: 1200px;
    height: 545px;
    background:
      radial-gradient(ellipse 55% 30% at 25% 35%, rgba(120, 90, 255, 0.18) 0%, transparent 70%),
      radial-gradient(ellipse 50% 35% at 80% 60%, rgba(110, 190, 255, 0.16) 0%, transparent 70%);
  }
  .slide-title {
    position: absolute;
    left: 0;
    right: 0;
    top: 60px;
    margin: 0;
    text-align: center;
    font-family: "Source Sans 3", "Myriad Pro", sans-serif;
    font-weight: 400;
    font-size: 57px;
    line-height: 1;
    color: var(--white);
    letter-spacing: 0.2px;
  }
  .version {
    position: absolute;
    top: 217px;
    width: 1200px;
    height: 349px;
    left: 0;
  }
  .version svg {
    position: absolute;
    left: 0;
    top: 0;
  }
  .hex-label {
    position: absolute;
    top: 0;
    width: 220px;
    text-align: center;
    font-family: "Manrope", sans-serif;
    font-weight: 500;
    color: var(--white);
  }
  .hex-label--old { left: 182px; }
  .hex-label--new { left: 798px; }
  .hex-label .word {
    display: block;
    margin-top: 64px;
    font-size: 80px;
    line-height: 80px;
    letter-spacing: -1px;
  }
  .hex-label .number {
    display: block;
    margin-top: 6px;
    font-size: 132px;
    line-height: 132px;
    letter-spacing: -4px;
  }
  .connector {
    position: absolute;
    left: 0;
    right: 0;
    top: 360px;
    text-align: center;
    font-family: "Source Sans 3", sans-serif;
    font-size: 52px;
    line-height: 1;
    color: var(--white);
  }
</style>
</head>
<body>
  <main class="slide">
    <div class="wave-texture" role="img" aria-label="Flowing dotted wave pattern in violet and light blue"></div>

    <h1 class="slide-title">What are the biggest differences between:</h1>

    <section class="version">
      <svg width="1200" height="349" viewBox="0 217 1200 349" aria-hidden="true">
        <polygon class="hex hex--old" points="190,217 393,217 492,391 393,566 190,566 89,391" fill="var(--green)"/>
        <polygon class="hex hex--new" points="806,217 1009,217 1109,391 1009,566 806,566 706,391" fill="var(--orange)"/>
      </svg>
      <p class="hex-label hex-label--old" style="margin:0"><span class="word">Web</span><span class="number">2.0</span></p>
      <p class="hex-label hex-label--new" style="margin:0"><span class="word">Web</span><span class="number">3.0</span></p>
    </section>

    <p class="connector" style="margin:0">to</p>
  </main>
</body>
</html>
```